Brivora Collective Business Card Design

We need a business card design for Brivora Collective. We are a healthcare recruiting, wellness and education company. We partner with medical facilities to find quality candidates. We also offer free wellness courses.
The final design should communicate an emphasis on recruiting and wellness
The main purpose of the business card is to utilized it for networking events, give to hospitals, executives, VCs surgery centers and clinics. I want it to be sleek, clean, use of our brand colors and professional.

```html
<!DOCTYPE html>
<html lang="en">
<head>
<meta charset="utf-8">
<title>Brivora Collective Business Card</title>
<link rel="stylesheet" href="https://fonts.googleapis.com/css2?family=Questrial&display=swap">
<style>
  :root {
    --brand: #0e5c55;
    --card: #ffffff;
    --backdrop: #e4e4e4;
  }
  * { margin: 0; padding: 0; box-sizing: border-box; }
  html, body { width: 1200px; height: 900px; overflow: hidden; }
  body {
    background: var(--backdrop);
    font-family: "Questrial", "Century Gothic", sans-serif;
    color: var(--brand);
    position: relative;
  }
  .card {
    position: absolute;
    top: 192px;
    width: 297px;
    height: 514px;
    background: var(--card);
    border-radius: 24px;
    box-shadow: 0 6px 14px rgba(0,0,0,0.18);
    overflow: hidden;
  }
  .card--front { left: 275px; }
  .card--back { left: 630px; }

  .wordmark { position: absolute; display: flex; align-items: center; }
  .wordmark__square {
    width: 22px; height: 22px;
    background: var(--brand);
    border-radius: 3px;
    flex-shrink: 0;
  }
  .wordmark__text { display: flex; flex-direction: column; line-height: 1; }
  .wordmark__name { font-size: 40px; letter-spacing: -0.5px; }
  .wordmark__sub { font-size: 20px; align-self: flex-end; margin-top: 2px; }

  .card--front .wordmark {
    left: 0; right: 0; top: 186px;
    flex-direction: column; gap: 18px;
  }
  .card--front .wordmark__square { width: 30px; height: 30px; }
  .card--front .wordmark__text { align-items: center; }
  .card--front .wordmark__sub { align-self: center; }

  .card--back .wordmark { left: 40px; top: 56px; gap: 14px; }
  .card--back .wordmark__name { font-size: 34px; }
  .card--back .wordmark__sub { font-size: 17px; }

  .person { position: absolute; left: 43px; top: 252px; }
  .person__name { font-size: 34px; line-height: 1.05; font-weight: 400; }
  .person__role { font-size: 15px; margin-top: 3px; }

  .contacts { position: absolute; left: 43px; top: 376px; list-style: none; font-size: 13.5px; line-height: 17px; }
  .contacts li { display: flex; align-items: flex-start; gap: 8px; }
  .contacts li.gap { margin-top: 10px; }
  .contacts svg { width: 11px; height: 11px; margin-top: 3px; flex-shrink: 0; fill: var(--brand); }
</style>
</head>
<body>
  <section class="card card--front">
    <div class="wordmark">
      <span class="wordmark__square"></span>
      <span class="wordmark__text">
        <span class="wordmark__name">Brivora</span>
        <span class="wordmark__sub">collective</span>
      </span>
    </div>
  </section>

  <section class="card card--back">
    <div class="wordmark">
      <span class="wordmark__square"></span>
      <span class="wordmark__text">
        <span class="wordmark__name">Brivora</span>
        <span class="wordmark__sub">collective</span>
      </span>
    </div>

    <div class="person">
      <h1 class="person__name">Maren<br>Holloway</h1>
      <p class="person__role">managing director</p>
    </div>

    <ul class="contacts">
      <li>
        <svg viewBox="0 0 12 12"><path d="M6 0a4 4 0 0 0-4 4c0 3 4 8 4 8s4-5 4-8a4 4 0 0 0-4-4zm0 5.6a1.6 1.6 0 1 1 0-3.2 1.6 1.6 0 0 1 0 3.2z"/></svg>
        <span>48 Linden Row<br>Eastvale, New York 10482</span>
      </li>
      <li>
        <svg viewBox="0 0 12 12"><path d="M3 0h6a1 1 0 0 1 1 1v10a1 1 0 0 1-1 1H3a1 1 0 0 1-1-1V1a1 1 0 0 1 1-1zm.8 1.5v7.5h4.4V1.5z"/></svg>
        <span>212 555 01 47</span>
      </li>
      <li>
        <svg viewBox="0 0 12 12"><path d="M3 0h6v3H3zM1 4h10a1 1 0 0 1 1 1v4H10v3H2V9H0V5a1 1 0 0 1 1-1zm2.5 5v1.8h5V9z"/></svg>
        <span>212 555 01 48</span>
      </li>
      <li class="gap">
        <svg viewBox="0 0 12 12"><path d="M0 2h12v1.2L6 7 0 3.2zM0 4.6l6 3.8 6-3.8V10H0z"/></svg>
        <span>info@brivoracollective.com</span>
      </li>
      <li>
        <svg viewBox="0 0 12 12"><circle cx="6" cy="6" r="5.3" fill="none" stroke="#0e5c55" stroke-width="1.2"/><ellipse cx="6" cy="6" rx="2.2" ry="5.3" fill="none" stroke="#0e5c55" stroke-width="1"/><path d="M0.8 6h10.4" stroke="#0e5c55" stroke-width="1"/></svg>
        <span>www.brivoracollective.com</span>
      </li>
    </ul>
  </section>
</body>
</html>
```